Agriculture Business Card

I want to use my existing logo and use my tagline of "Don't Guess...Soil Test" on the card. Looking for a double sided card that will really get peoples attention.
Contact Info:
Brisco Harvest Crop Solutions
Calvin Brisco
2917 K Lane
Otoe, NE 68539
402-815-2493
calvin.r.brisco@furrowpost.net

```html
<!DOCTYPE html>
<html lang="en">
<head>
<meta charset="utf-8">
<title>Brisco Harvest Crop Solutions – Business Card</title>
<link rel="stylesheet" href="https://fonts.googleapis.com/css2?family=Oswald:wght@400;500;700&display=swap">
<style>
  :root {
    --bg: #ebe9e7;
    --soil: #553733;
    --harvest: #f0b01a;
    --harvest-deep: #e09a10;
    --field: #35a94a;
    --paper: #f4f3f1;
    --white: #ffffff;
  }
  * { margin: 0; padding: 0; box-sizing: border-box; }
  html, body { width: 1200px; height: 900px; overflow: hidden; }
  body {
    background: var(--bg);
    font-family: "Oswald", "Arial Narrow", sans-serif;
    position: relative;
  }
  .card {
    position: absolute;
    left: 320px;
    width: 560px;
    height: 320px;
    overflow: hidden;
    box-shadow: 0 10px 28px rgba(0,0,0,0.18);
  }

  /* Back side */
  .card-back { top: 70px; background: var(--soil); }
  .tagline-lead {
    position: absolute; left: 48px; top: 66px;
    color: var(--harvest); font-weight: 700; font-size: 32px;
    text-transform: uppercase; letter-spacing: 0.5px; line-height: 1;
  }
  .tagline-main {
    position: absolute; left: 44px; top: 104px;
    color: var(--white); font-weight: 700; font-size: 90px;
    text-transform: uppercase; line-height: 1; letter-spacing: 1px;
    white-space: nowrap;
  }
  .flask-art {
    position: absolute; left: 438px; top: 150px;
    width: 76px; height: 124px;
  }

  /* Front side */
  .card-front { top: 490px; background: var(--paper); }
  .front-shapes { position: absolute; inset: 0; }
  .holder-name {
    position: absolute; left: 30px; top: 44px;
    color: var(--soil); font-weight: 700; font-size: 38px;
    text-transform: uppercase; line-height: 1; letter-spacing: 0.5px;
    white-space: nowrap;
  }
  .holder-role {
    position: absolute; left: 32px; top: 90px;
    color: var(--white); font-weight: 500; font-size: 20px;
    text-transform: uppercase; letter-spacing: 1px; line-height: 1;
  }
  .contact-list {
    position: absolute; left: 16px; top: 190px;
    list-style: none; color: var(--white);
    font-size: 12px; line-height: 1.9; letter-spacing: 0.2px;
    white-space: nowrap;
  }
  .contact-list li, .contact-address { display: flex; align-items: center; gap: 6px; }
  .contact-address {
    position: absolute; left: 190px; top: 193px;
    color: var(--white); font-size: 12px; line-height: 1.5;
    white-space: nowrap;
  }
  .icon { width: 14px; height: 14px; flex: none; }
  .brand {
    position: absolute; left: 345px; top: 120px; width: 190px;
    display: flex; align-items: center; gap: 10px;
  }
  .brand-dot { width: 18px; height: 18px; border-radius: 50%; background: var(--harvest); flex: none; }
  .brand-name {
    color: var(--soil); font-weight: 500; font-size: 22px; line-height: 1.15;
  }
</style>
</head>
<body>

  <section class="card card-back" aria-label="Card back">
    <p class="tagline-lead">Don't Guess...</p>
    <p class="tagline-main">Soil Test</p>
    <svg class="flask-art" role="img" aria-label="Illustration of a lab flask filled with soil and a sprouting seedling" viewBox="0 0 76 124">
      <defs>
        <linearGradient id="flaskFill" x1="0" y1="0" x2="0" y2="1">
          <stop offset="0" stop-color="var(--harvest)"/>
          <stop offset="1" stop-color="var(--harvest-deep)"/>
        </linearGradient>
      </defs>
      <rect x="0" y="0" width="76" height="124" fill="url(#flaskFill)" rx="4"/>
    </svg>
  </section>

  <section class="card card-front" aria-label="Card front">
    <svg class="front-shapes" viewBox="0 0 560 320" preserveAspectRatio="none" aria-hidden="true">
      <polygon points="0,0 318,0 282,320 0,320" fill="var(--harvest)"/>
      <polygon points="0,180 300,180 295,250 0,250" fill="var(--field)"/>
      <polygon points="318,0 324,0 288,320 282,320" fill="var(--soil)"/>
    </svg>

    <h1 class="holder-name">Calvin Brisco</h1>
    <p class="holder-role">Owner</p>

    <ul class="contact-list">
      <li>
        <svg class="icon" viewBox="0 0 16 16" aria-hidden="true"><circle cx="8" cy="8" r="8" fill="#fff"/><path d="M5.2 4.2l1.4-.3.8 2-1 .7a5 5 0 0 0 2.9 2.9l.7-1 2 .8-.3 1.4c-3.5.4-6.9-3-6.5-6.5z" fill="var(--field)"/></svg>
        <span>402-815-2493</span>
      </li>
      <li>
        <svg class="icon" viewBox="0 0 16 16" aria-hidden="true"><circle cx="8" cy="8" r="8" fill="#fff"/><rect x="4" y="5" width="8" height="6" fill="var(--field)"/><path d="M4 5l4 3.2L12 5" stroke="#fff" stroke-width="1" fill="none"/></svg>
        <span>calvin.r.brisco@furrowpost.net</span>
      </li>
    </ul>

    <div class="contact-address">
      <svg class="icon" viewBox="0 0 16 16" aria-hidden="true"><circle cx="8" cy="8" r="8" fill="#fff"/><path d="M8 3.5a3 3 0 0 0-3 3c0 2.2 3 5.8 3 5.8s3-3.6 3-5.8a3 3 0 0 0-3-3z" fill="var(--field)"/><circle cx="8" cy="6.5" r="1.1" fill="#fff"/></svg>
      <span>2917 K Lane<br>Otoe, NE 68539</span>
    </div>

    <div class="brand">
      <span class="brand-dot" aria-hidden="true"></span>
      <span class="brand-name">Brisco Harvest Crop Solutions</span>
    </div>
  </section>

</body>
</html>
```